Interior designer needs a gorgeous, chic business card design.

A new, small Interior Design firm needs a business card that is chic, contemporary and elegant. Nothing over the top. My interiors are contemporary classic with an elegant feel to them. I like to use quality finishes and products rather than follow the latest fads. Projects can be anything from Pre start selections, bathrooms, kitchens, bedrooms, custom upholstery, furniture, rugs and art etc. The final design should display quality and an achievable sense of chic. I am open to all colours including black but not limited to this.

```html
<!DOCTYPE html>
<html lang="en">
<head>
<meta charset="utf-8">
<title>Marlo Interiors – Business Card</title>
<link href="https://fonts.googleapis.com/css2?family=Cinzel:wght@400&display=swap" rel="stylesheet">
<style>
  :root {
    --backdrop: #e8e6e2;
    --card-white: #ffffff;
    --ink: #111111;
    --band: #0d0d0d;
    --paper-light: #fbf9f4;
    --paper-gold: #ece4d2;
    --back-dark: #0e0e0e;
    --back-pattern: #1d1d1d;
    --text-light: #f4f4f4;
    --rule: #222222;
  }
  * { box-sizing: border-box; margin: 0; padding: 0; }
  html, body {
    width: 1200px; height: 849px; overflow: hidden;
    background: var(--backdrop);
    font-family: "Cinzel", "Times New Roman", serif;
  }
  .canvas {
    position: relative; width: 1200px; height: 849px;
    display: flex; align-items: center; justify-content: center; gap: 60px;
  }
  .card {
    position: relative; width: 520px; height: 297px; overflow: hidden;
    box-shadow: 0 8px 24px rgba(0,0,0,0.18);
  }
  .card-pattern { position: absolute; inset: 0; width: 100%; height: 100%; display: block; }

  /* Front */
  .card-front { background: var(--card-white); }
  .front-band {
    position: absolute; left: 0; right: 0; bottom: 0; height: 96px;
    background: var(--band);
  }
  .contact-list {
    position: absolute; left: 150px; bottom: 20px;
    list-style: none; color: var(--text-light);
    font-size: 11px; letter-spacing: 0.06em; line-height: 19px;
  }
  .logo-frame {
    position: absolute; left: 26px; bottom: 118px;
    padding: 10px 16px; border: 1px solid var(--rule);
    background: var(--card-white);
  }
  .logo-name {
    font-size: 19px; letter-spacing: 0.08em; color: var(--ink); white-space: nowrap;
  }
  .person {
    position: absolute; right: 28px; bottom: 116px; text-align: right;
    color: var(--ink); font-size: 12.5px; letter-spacing: 0.05em; line-height: 18px;
  }
  .person-name { font-size: 14px; }

  /* Back */
  .card-back { background: var(--back-dark); }
  .back-content {
    position: absolute; inset: 0;
    display: flex; flex-direction: column; align-items: center; justify-content: center; gap: 18px;
    color: var(--text-light);
  }
  .back-logo { font-size: 28px; letter-spacing: 0.1em; }
  .back-web { font-size: 11px; letter-spacing: 0.12em; }
</style>
</head>
<body>
<main class="canvas">

  <section class="card card-front" aria-label="Business card front">
    <svg class="card-pattern" viewBox="0 0 520 297" preserveAspectRatio="none" role="img" aria-label="Gold damask pattern on white">
      <defs>
        <linearGradient id="damask-light" x1="0" y1="0" x2="1" y2="1">
          <stop offset="0" stop-color="var(--paper-light)"/>
          <stop offset="1" stop-color="var(--paper-gold)"/>
        </linearGradient>
      </defs>
      <rect width="520" height="297" fill="url(#damask-light)"/>
    </svg>
    <div class="logo-frame">
      <span class="logo-name">MARLO INTERIORS</span>
    </div>
    <div class="person">
      <p class="person-name">ELISE MARLO HART</p>
      <p>(DIP. INTERIOR DESIGN)</p>
      <p>DIRECTOR</p>
    </div>
    <div class="front-band">
      <ul class="contact-list">
        <li>MOB: 0412345678</li>
        <li>EMAIL: ELISE@MARLOINTERIORS.COM.AU</li>
        <li>WWW.MARLOINTERIORS.COM</li>
      </ul>
    </div>
  </section>

  <section class="card card-back" aria-label="Business card back">
    <svg class="card-pattern" viewBox="0 0 520 297" preserveAspectRatio="none" role="img" aria-label="Dark tone-on-tone damask pattern on black">
      <defs>
        <radialGradient id="damask-dark" cx="0.5" cy="0.5" r="0.75">
          <stop offset="0" stop-color="var(--back-pattern)"/>
          <stop offset="1" stop-color="var(--back-dark)"/>
        </radialGradient>
      </defs>
      <rect width="520" height="297" fill="url(#damask-dark)"/>
    </svg>
    <div class="back-content">
      <p class="back-logo">MARLO INTERIORS</p>
      <p class="back-web">WWW.MARLOINTERIORS.COM</p>
    </div>
  </section>

</main>
</body>
</html>
```